Infografik für Tanzschule
Zielgruppe
Wir sind eine Tanzschule für die Tänze Salsa, Bachata, kizomba & Zouk in Freiburg
Aufgabenstellung
DESIGN-BRIEFING
Tarifübersicht – Tanzschule Ritmo del Alba
Projektziel
Gestaltung einer klaren, hochwertigen Tarifübersicht für eine Tanzschule.
Die Grafik dient: als Information & Orientierung auf der Homepage, als visuelle Grundlage für das Anmeldeformular vor Ort, Der Einstieg erfolgt immer über eine gratis Schnupperstunde.
Die verbindliche Anmeldung erfolgt nach der Schnupperstunde vor Ort über ein Formular mit Auswahlkästchen.
Grundaufbau
3 Tarifkarten nebeneinander
Einheitlicher, moderner Stil
evtl. Emotionale Bilder (echte Tanzszenen, echte Menschen)
Klare Hierarchie:
Titel → Preis → Erklärung → Vorteile → Auswahlkästchen
Struktur der Tarifkarten
KARTE 1 – EINSTIEG
Titel: 1× PRO WOCHE TANZEN
Preis: 56 €/ 39 € erm.
Subline: pro Person · pro Kalendermonat
Vorteile (max. 4 Bulletpoints):
Ein fester wöchentlicher Kurs
Klare Routine & Struktur
Ausweichstunde im selben Monat möglich (muss klar enthalten sein)
Auswahl: ☐ 1× pro Woche tanzen
KARTE 2 – REGELMÄSSIG TANZEN (darf visuell leicht hervorgehoben sein, z. B. Rahmen oder Badge)
Optionales Badge:
SEHR BELIEBT
Titel: 2× PRO WOCHE TANZEN
Preis: 98 € / 68 € erm.
Vorteile:
Zwei feste wöchentliche Kurse
Mehr Praxis & schnellerer Fortschritt
Ausweichstunde im selben Monat möglich
Auswahl:
☐ 2× pro Woche tanzen
KARTE 3 – MAXIMALE FREIHEIT
Titel: FLAT – ALL YOU CAN DANCE
Preis: ab 129 € / 99 € erm.
Alle Tänze
Alle Kurse (für dein Tanz-Level)
Alle Workshops (für dein Tanz-Level)
Maximale Freiheit
☐ FLAT 1 Monat – 149 € | 119 € erm. (monatlich kündbar)
☐ FLAT 3 Monate – 129 € | 99 € erm. (3 Monate Erstlaufzeit)
Einheitlicher Hinweis unter den Karten (kleiner Text)
Ausweic..

```html
<!DOCTYPE html>
<html lang="de">
<head>
<meta charset="utf-8">
<title>Anmeldeformular – Ritmo del Alba</title>
<link rel="stylesheet" href="https://fonts.googleapis.com/css2?family=Inter+Tight:ital,wght@0,400;0,500;0,600;0,700;1,400&family=Barlow+Condensed:wght@400;500;600&display=swap">
<style>
:root{
  --bg:#c9c9c9;
  --paper:#ffffff;
  --ink:#2b2b2b;
  --muted:#5c5c5c;
  --line:#9a9a9a;
  --card:#f2f2f2;
  --card-border:#dcdcdc;
  --accent:#333333;
  --band:#dde5df;
  --photo-a:#8c95a8;
  --photo-b:#b7a99a;
  --photo-c:#5f6f52;
}
*{box-sizing:border-box;margin:0;padding:0}
html,body{width:722px;height:1200px;overflow:hidden;background:var(--bg)}
body{font-family:"Inter Tight",sans-serif;color:var(--ink)}
.sheet{position:absolute;left:21px;top:120px;width:680px;height:960px;background:var(--paper);box-shadow:0 10px 24px rgba(0,0,0,.25);overflow:hidden}
.abs{position:absolute}
.header-photo{left:0;top:0;width:680px;height:141px;background:linear-gradient(180deg,var(--photo-a) 0%,var(--photo-b) 55%,var(--photo-c) 100%)}
.form-title{left:36px;top:12px;font-size:18px;font-weight:700;color:#fff;letter-spacing:-.3px}
.brand{right:46px;top:104px;color:#fff;font-size:13px;font-weight:500;display:flex;align-items:center;gap:6px}
.brand .dot{width:9px;height:9px;border-radius:50%;background:#fff}
.box{display:inline-block;width:8px;height:8px;border:1px solid var(--ink);border-radius:1px;vertical-align:-1px}
.personal{left:41px;top:161px;width:425px;font-size:10px;color:var(--muted)}
.salutation{display:flex;gap:4px;align-items:center;margin-bottom:7px}
.field{display:flex;align-items:flex-end;height:23px}
.field .label{width:110px}
.field .colon{width:6px}
.field .rule{flex:1;border-bottom:1px solid var(--line);height:12px}
.opt{margin-top:6px;display:flex;gap:6px;align-items:center}
.contact{left:498px;top:165px;width:145px;height:166px;border:1px solid #e3e3e3;border-radius:6px;background:#f7f7f7;padding:13px 6px;font-size:9px;line-height:12.5px;color:var(--muted)}
.contact b{color:var(--ink);font-weight:600}
.contact .gap{height:14px}
.card{top:361px;width:197px;height:297px;background:var(--card);border:1px solid var(--card-border);border-radius:6px;padding:12px 11px}
.card.featured{background:#fff;border:1.5px solid var(--accent)}
.badge{position:absolute;top:-9px;left:50%;transform:translateX(-50%);background:var(--accent);color:#fff;font-size:9.5px;font-weight:500;padding:1px 9px;border-radius:8px}
.card h2{font-size:17px;line-height:18px;font-weight:600;letter-spacing:-.4px}
.price{margin-top:14px;font-family:"Barlow Condensed",sans-serif;display:flex;align-items:baseline;gap:2px}
.price sup{font-size:10px;align-self:flex-start;margin-top:2px}
.price .num{font-size:33px;font-weight:600;line-height:30px}
.price .red{font-size:11px;font-weight:500;margin-left:4px}
.per{font-size:10px;color:var(--muted);padding-bottom:8px;border-bottom:1px solid #cfcfcf;margin-top:4px}
.perks-title{font-size:10.5px;font-weight:600;margin-top:10px;margin-bottom:3px}
.perks{list-style:none;font-size:9.6px;color:var(--muted);line-height:13px}
.perks li{display:flex;gap:5px;margin-bottom:3px;max-width:160px}
.perks svg{flex:none;margin-top:2px}
.choice{border-top:1px solid #cfcfcf;margin-top:10px;padding-top:8px;font-size:10px;font-weight:500}
.choice div{display:flex;gap:6px;align-items:center}
.choice .note{font-size:9px;font-style:italic;color:var(--muted);font-weight:400;margin:2px 0 8px}
.notes{top:682px;font-size:10px}
.notes h3{font-size:10.5px;font-weight:600;margin-bottom:3px}
.notes p{border-left:1px solid #bbb;padding-left:9px;font-style:italic;color:var(--muted);font-size:10px;line-height:13.5px}
.band{left:0;top:748px;width:680px;height:212px;background:var(--band)}
.sepa{left:36px;top:761px;width:607px;height:117px;background:#fff;padding:6px 10px;font-family:"Barlow Condensed",sans-serif}
.sepa h4{font-size:9.5px;font-weight:600}
.sepa p{font-size:7.7px;line-height:9.6px;color:var(--muted);letter-spacing:-.15px}
.bank{margin-top:5px;border:1px solid var(--ink);font-size:8px}
.bank .row1{display:flex;height:26px;border-bottom:1px solid var(--ink)}
.bank .row1 div{padding:2px 5px}
.bank .row1 div:first-child{width:341px;border-right:1px solid var(--ink)}
.iban{display:flex;height:26px;align-items:flex-end;padding:2px 5px}
.iban .lbl{width:26px;align-self:flex-start}
.iban .cell{width:23.5px;height:14px;border-left:1px solid var(--ink);font-size:13px;text-align:center;line-height:14px}
.iban .cell.wide{border-left-width:1.4px;height:17px}
.months{left:36px;top:893px;width:244px;height:29px;background:#fff;display:flex;justify-content:space-around;padding:3px 6px;font-family:"Barlow Condensed",sans-serif;font-size:7.5px;font-weight:600}
.months span{display:flex;flex-direction:column;align-items:center;gap:1px}
.months .box{width:8px;height:8px}
.sign{left:359px;top:893px;width:284px;height:36px;background:#fff}
.foot{font-family:"Barlow Condensed",sans-serif;font-size:13px;font-weight:500}
.foot small{font-size:7.5px;font-weight:600}
</style>
</head>
<body>
<main class="sheet">
  <div class="abs header-photo" role="img" aria-label="Gruppenfoto der Tanzlehrerinnen und Tanzlehrer auf einer Terrasse über der Stadt mit Kirchturm"></div>
  <h1 class="abs form-title">Anmeldeformular</h1>
  <div class="abs brand"><span class="dot"></span>Ritmo del Alba</div>

  <section class="abs personal">
    <div class="salutation">Frau <span class="box"></span> Herr <span class="box"></span> Div. <span class="box"></span></div>
    <div class="field"><span class="label">Vorname / Nachname</span><span class="colon">:</span><span class="rule"></span></div>
    <div class="field"><span class="label">Straße / Nr</span><span class="colon">:</span><span class="rule"></span></div>
    <div class="field"><span class="label">PLZ/Ort</span><span class="colon">:</span><span class="rule"></span></div>
    <div class="field"><span class="label">Telefon</span><span class="colon">:</span><span class="rule"></span></div>
    <div class="field"><span class="label">E-mail</span><span class="colon">:</span><span class="rule"></span></div>
    <div class="opt" style="margin-top:12px"><span class="box"></span>Ermäßigt (Student*in / Schüler*in / Auszubildende*r)</div>
    <div class="opt"><span class="box"></span>Ja, ich möchte den Newsletter und Kursinformationen erhalten.</div>
  </section>

  <aside class="abs contact">
    <b>Tanzschule Ritmo del Alba</b><br>Lindenweg 14 79312 Emmendingen
    <div class="gap"></div>
    <b>Geschäftsanschrift</b><br>Ritmo del Alba Lena Hartwig<br>Mühlgasse 8 79312 Emmendingen
    <div class="gap"></div>
    <b>T</b> : +49 151 480 226 19<br><b>M</b> : info@ritmo-del-alba.de<br><b>W</b> : www.ritmo-del-alba.de
  </aside>

  <article class="abs card" style="left:36px">
    <h2>1× Pro Woche<br>Tanzen</h2>
    <div class="price"><sup>€</sup><span class="num">56</span><span class="red">/ 39 € erm.</span></div>
    <div class="per">pro Person / Kalendermonat</div>
    <div class="perks-title">Vorteile</div>
    <ul class="perks">
      <li><svg width="8" height="8" viewBox="0 0 8 8"><rect x=".5" y=".5" width="7" height="7" fill="none" stroke="#555"/><path d="M2 4l1.5 1.5L6 2.5" fill="none" stroke="#555"/></svg>Ein fester wöchentlicher Kurs</li>
      <li><svg width="8" height="8" viewBox="0 0 8 8"><rect x=".5" y=".5" width="7" height="7" fill="none" stroke="#555"/><path d="M2 4l1.5 1.5L6 2.5" fill="none" stroke="#555"/></svg>Klare Routine &amp; Struktur</li>
      <li><svg width="8" height="8" viewBox="0 0 8 8"><rect x=".5" y=".5" width="7" height="7" fill="none" stroke="#555"/><path d="M2 4l1.5 1.5L6 2.5" fill="none" stroke="#555"/></svg>Ausweichstunde im selben Monat möglich</li>
    </ul>
    <div class="choice" style="margin-top:26px"><div><span class="box"></span>1× pro Woche tanzen</div></div>
  </article>

  <article class="abs card featured" style="left:241px">
    <span class="badge">Sehr Beliebt</span>
    <h2>Regelmässig<br>Tanzen</h2>
    <div class="price"><sup>€</sup><span class="num">98</span><span class="red">/ 68 € erm.</span></div>
    <div class="per">pro Person / Kalendermonat</div>
    <div class="perks-title">Vorteile</div>
    <ul class="perks">
      <li><svg width="8" height="8" viewBox="0 0 8 8"><rect x=".5" y=".5" width="7" height="7" fill="none" stroke="#555"/><path d="M2 4l1.5 1.5L6 2.5" fill="none" stroke="#555"/></svg>Zwei feste wöchentliche Kurse</li>
      <li><svg width="8" height="8" viewBox="0 0 8 8"><rect x=".5" y=".5" width="7" height="7" fill="none" stroke="#555"/><path d="M2 4l1.5 1.5L6 2.5" fill="none" stroke="#555"/></svg>Mehr Praxis &amp; schnellerer<br>Fortschritt</li>
      <li><svg width="8" height="8" viewBox="0 0 8 8"><rect x=".5" y=".5" width="7" height="7" fill="none" stroke="#555"/><path d="M2 4l1.5 1.5L6 2.5" fill="none" stroke="#555"/></svg>Ausweichstunde im selben Monat möglich</li>
    </ul>
    <div class="choice"><div><span class="box"></span>2× pro Woche tanzen</div></div>
  </article>

  <article class="abs card" style="left:446px">
    <h2>Flat – All You Can<br>Dance</h2>
    <div class="price"><sup>ab</sup><span class="num">129</span><sup>€</sup><span class="red">/ 99 € erm.</span></div>
    <div class="per">pro Person / Kalendermonat</div>
    <div class="perks-title">Vorteile</div>
    <ul class="perks">
      <li><svg width="8" height="8" viewBox="0 0 8 8"><rect x=".5" y=".5" width="7" height="7" fill="none" stroke="#555"/><path d="M2 4l1.5 1.5L6 2.5" fill="none" stroke="#555"/></svg>Alle Tänze</li>
      <li><svg width="8" height="8" viewBox="0 0 8 8"><rect x=".5" y=".5" width="7" height="7" fill="none" stroke="#555"/><path d="M2 4l1.5 1.5L6 2.5" fill="none" stroke="#555"/></svg>Alle Kurse (für dein Tanz-Level)</li>
      <li><svg width="8" height="8" viewBox="0 0 8 8"><rect x=".5" y=".5" width="7" height="7" fill="none" stroke="#555"/><path d="M2 4l1.5 1.5L6 2.5" fill="none" stroke="#555"/></svg>Alle Workshops (für dein Tanz-<br>Level)</li>
      <li><svg width="8" height="8" viewBox="0 0 8 8"><rect x=".5" y=".5" width="7" height="7" fill="none" stroke="#555"/><path d="M2 4l1.5 1.5L6 2.5" fill="none" stroke="#555"/></svg>Maximale Freiheit</li>
    </ul>
    <div class="choice" style="margin-top:7px">
      <div><span class="box"></span>FLAT 1 Monat – 149 € | 119 € erm.</div>
      <p class="note">(monatlich kündbar)</p>
      <div><span class="box"></span>FLAT 3 Monate – 129 € | 99 € erm.</div>
      <p class="note">(3 Monate Erstlaufzeit)</p>
    </div>
  </article>

  <section class="abs notes" style="left:36px;width:160px">
    <h3>Hinweis</h3>
    <p>Ausweichstunde: im selben Kalendermonat möglich.</p>
  </section>
  <section class="abs notes" style="left:241px;width:402px">
    <h3>Verlängerung &amp; Kündigung</h3>
    <p>Der Vertrag verlängert sich automatisch um jeweils einen Monat und ist mit 14 Tagen<br>Frist zum Monatsende kündbar.<br>Ausnahme: FLAT 3 Monate – kündbar nach Ablauf der Erstlaufzeit.</p>
  </section>

  <div class="abs band"></div>
  <section class="abs sepa">
    <h4>Einzugsermächtigung / SEPA-Lastschriftmandat</h4>
    <p>Ich ermächtige Ritmo del Alba, Zahlungen von meinem Konto per Lastschrift einzuziehen und mein Kreditinstitut, diese Lastschriften einzulösen. Bei Ablehnung der Lastschrift fallen Kosten von 10,00 € pro Rückbuchung an. Ich kann innerhalb von acht Wochen ab Belastungsdatum die Erstattung verlangen, gemäß den Bedingungen meines Kreditinstituts. Die Kursgebühr wird im ersten Monat zur Mitte/Ende eingezogen, danach jeweils am 05. jedes Monats.</p>
    <div class="bank">
      <div class="row1"><div>Kreditinstitut:</div><div>BIC: - Beginnt die IBAN mit DE, dann ist kein BIC nötig</div></div>
      <div class="iban">
        <span class="lbl">IBAN:</span>
        <span class="cell">D</span><span class="cell">E</span><span class="cell"></span><span class="cell"></span><span class="cell wide"></span><span class="cell"></span><span class="cell"></span><span class="cell"></span><span class="cell wide"></span><span class="cell"></span><span class="cell"></span><span class="cell"></span><span class="cell wide"></span><span class="cell"></span><span class="cell"></span><span class="cell"></span><span class="cell wide"></span><span class="cell"></span><span class="cell"></span><span class="cell"></span><span class="cell wide"></span><span class="cell"></span><span class="cell"></span><span class="cell" style="border-right:1px solid var(--ink)"></span>
      </div>
    </div>
  </section>

  <div class="abs months">
    <span>Jan<i class="box"></i></span><span>Feb<i class="box"></i></span><span>Mrz<i class="box"></i></span><span>Apr<i class="box"></i></span><span>Mai<i class="box"></i></span><span>Jun<i class="box"></i></span><span>Jul<i class="box"></i></span><span>Aug<i class="box"></i></span><span>Sep<i class="box"></i></span><span>Okt<i class="box"></i></span><span>Nov<i class="box"></i></span><span>Dez<i class="box"></i></span>
  </div>
  <div class="abs sign"></div>
  <div class="abs foot" style="left:36px;top:929px">Kursstart / Anmeldung ab:</div>
  <div class="abs foot" style="left:359px;top:935px">Datum / Unterschrift: <small>Wir verweisen auf unsere umseitig abgedruckten AGB</small></div>
</main>
</body>
</html>
```